IV Nutritional Clinic Web Design

We are working with Velmo. They are an IV Nutritional Clinic and in need of a new website design.
Some sites to use for inspiration:
https://brightpathcare.example
https://www.mylumarowellness.example
https://www.quenchlounge.example
https://vitrapulse.example
https://www.sola-vita.example/pages/iv-therapy-west-hollywood
https://www.gtoncologycare.example/cancer-care/iv-drips/
https://dripfuelwell.example
https://thrivoramedclinic.example
Thank you for taking the time to consider designing a website for us. We are web developers based in Stockton, CA, USA. Most of our projects go through the same process. Understanding this process may help you win a project with us. We custom-code all of our websites in-house. We don’t have any requirements as to what tools you use for your design, but we prefer Figma files. For any design that we label as four-stars, we send it to the client for review. The client picks the final design they want us to use. Once we complete this process, we will continue to show additional clients all the four-star sites and purchase them later. Your designs will have multiple chances to sell. For better chances of success, we ask that you follow these guidelines.
IMAGES:
If you use any images or icons in the design, we ask that you have a link to the asset so we can purchase the image/icon. Most of the designs we submit do not have the customer’s images on them unless they have some great images. Be creative; show us the feeling you are trying to portray with your image choices. Use any royalty-free site you choose. We subscribe to Korvane and mainly use their images, but we can purchase images outside of Korvane.
PLEASE NOTE: we will not submit designs to clients with watermarks on the images.
FONTS:
We ask that you identify the fonts used in the design. This can be done in a message if you want. We typically use Tessly Type and Korvane Type.
CONTENT:
We're always open to different content and ideas. We often submit designs with stock images so the client can see our vision. We typically take pictures after the website launch to use their images with our vision. Lorem Ipsum is fine for paragraphs, but we ask that you write the headers in correct English. We want to be able to show the vision and identify the sections of the website.
INSPIRATION:
We typically add a couple of links in the brief of websites we like to help you get started in your design.
REVISIONS:
We do not often ask for revisions of the designs unless we see something in the design that may not appeal to the client. If there are slight changes that we want to make, we do that in the development process.
FEEDBACK:
We rarely give feedback on designs during the design process. We are working on many website projects and do not have the time to provide feedback. We usually respond if your request is well thought out and asks specific questions, but a note asking “feedback, please” usually goes unanswered.

```html
<!DOCTYPE html>
<html lang="en">
<head>
<meta charset="utf-8">
<title>Velmo Hydration – IV Nutritional Clinic</title>
<link href="https://fonts.googleapis.com/css2?family=Montserrat:wght@600;700;800&family=Open+Sans:ital,wght@0,400;0,600;0,700;1,400&display=swap" rel="stylesheet">
<style>
:root{
  --navy:#1f2a7a;
  --green:#7cae3f;
  --text:#3a3f4f;
  --muted:#666b78;
  --soft:#f1f3f9;
  --white:#ffffff;
  --line:#dde1ea;
}
*{box-sizing:border-box;margin:0;padding:0}
html,body{width:1200px;height:4648px;overflow:hidden}
body{font-family:"Open Sans",Arial,sans-serif;color:var(--text);background:var(--white);position:relative}
h1,h2,h3,.logo,.btn{font-family:"Montserrat",Arial,sans-serif}
.btn{display:inline-block;background:var(--green);color:var(--white);font-size:12px;font-weight:700;letter-spacing:.5px;text-transform:uppercase;padding:12px 28px;border-radius:22px;text-decoration:none;white-space:nowrap}
.btn.outline{background:var(--white);color:var(--navy);border:2px solid var(--line)}
.photo{display:block}

/* header + hero */
.hero{position:absolute;left:0;top:0;width:1200px;height:564px;background:linear-gradient(90deg,#f6f8fc 0%,#eef2f8 45%,#dfe6ef 70%,#f3e6dc 100%)}
.hero-photo{position:absolute;right:0;top:0;width:640px;height:564px;background:linear-gradient(100deg,rgba(246,248,252,1) 0%,rgba(226,232,240,.6) 30%,#e9dfd6 65%,#d7c6b7 100%)}
.topbar{position:absolute;top:10px;left:300px;width:800px;display:flex;justify-content:space-between;font-size:12px;color:var(--navy)}
.topbar .phone{display:flex;align-items:center;gap:6px}
.logo{position:absolute;left:96px;top:44px;display:flex;align-items:center;gap:12px;font-size:56px;line-height:1;font-weight:800;color:var(--navy);letter-spacing:2px}
.logo .mark{width:20px;height:20px;background:var(--green);border-radius:50%}
.nav{position:absolute;top:97px;left:400px;display:flex;gap:26px;font-size:12px;font-weight:700;color:var(--navy);text-transform:uppercase}
.book-now{position:absolute;left:1000px;top:88px;padding:10px 24px;font-size:11px}
.hero h1{position:absolute;left:96px;top:228px;font-size:54px;line-height:1.1;color:var(--navy);font-weight:800;width:640px}
.hero .lead{position:absolute;left:96px;top:366px;font-size:16px;line-height:1.45;color:var(--navy);width:400px}
.hero .cta{position:absolute;left:96px;top:432px}

/* service cards */
.services{position:absolute;top:564px;left:96px;width:1008px;display:flex;gap:16px}
.service{width:240px;height:216px;position:relative}
.service .photo{width:100%;height:100%}
.service span{position:absolute;left:0;bottom:0;width:100%;height:46px;background:rgba(255,255,255,.85);color:var(--navy);font-size:16px;display:flex;align-items:center;justify-content:center}
.service.active span{background:var(--navy);color:var(--white)}

/* intro */
.intro{position:absolute;top:896px;left:140px;width:920px;text-align:center}
.intro h2{font-family:"Open Sans",Arial,sans-serif;font-weight:600;font-size:22px;line-height:1.4;color:var(--navy)}
.intro p{margin-top:20px;font-size:14px;line-height:1.6;color:var(--muted);padding:0 60px}
.intro .actions{margin-top:32px;display:flex;justify-content:center;gap:24px}

/* why choose */
.why{position:absolute;top:1248px;left:0;width:1200px;height:2376px;background:var(--soft)}
.section-title{position:absolute;left:0;width:100%;font-size:20px;font-weight:800;color:var(--navy);text-align:center;letter-spacing:1px;text-transform:uppercase}
.why .section-title{top:84px}
.feature{position:absolute;left:96px;width:1008px;display:flex;align-items:center;gap:44px}
.feature .photo{width:480px;height:300px;flex:none}
.feature .copy{width:484px}
.feature h3{font-size:26px;line-height:1.15;color:var(--navy);font-weight:800;text-transform:uppercase}
.feature p{margin-top:16px;font-size:14px;line-height:1.6;color:var(--text)}
.feature .btn{margin-top:22px}
.feature.reverse .copy{order:-1}
.f1{top:192px}.f2{top:632px}.f3{top:1064px}.f4{top:1492px}.f5{top:1932px}

/* testimonials */
.reviews{position:absolute;top:3624px;left:0;width:1200px;height:676px;background:var(--white)}
.reviews .section-title{top:184px}
.review-row{position:absolute;top:272px;left:96px;width:1008px;display:flex;gap:64px}
.review{width:472px;height:250px;background:var(--white);box-shadow:0 4px 18px rgba(31,42,122,.12);padding:28px 36px}
.review h4{font-size:15px;font-weight:600;color:var(--text)}
.review p{margin-top:12px;font-style:italic;font-size:14px;line-height:1.5;color:var(--text)}
.author{margin-top:16px;display:flex;align-items:center;gap:16px}
.avatar{width:50px;height:50px;border-radius:50%;background:linear-gradient(135deg,#e6cfb8,#b89880)}
.author b{display:block;font-style:italic;font-weight:400;font-size:14px}
.author i{font-size:13px;color:var(--muted)}
.dots{position:absolute;top:560px;left:0;width:100%;display:flex;justify-content:center;gap:10px}
.dots span{width:16px;height:16px;border-radius:50%;background:#9aa0ad}
.dots span.on{background:var(--green)}

/* footer */
.footer{position:absolute;top:4300px;left:0;width:1200px;height:260px;background:var(--soft)}
.footer .logo{top:84px}
.fcol{position:absolute;top:40px;font-size:12px;line-height:2;color:var(--text);text-transform:uppercase}
.fcol h5{font-size:12px;font-weight:700;color:var(--navy);margin-bottom:6px;text-transform:uppercase}
.fcol.links{left:436px}
.fcol.links ul{display:grid;grid-template-columns:110px 110px;list-style:none}
.fcol.reach{left:720px;text-transform:none}
.fcol.social{left:940px}
.socials{display:flex;gap:12px;margin-top:6px}
.socials span{width:20px;height:20px;background:var(--navy);border-radius:3px}
.copyright{position:absolute;top:4560px;left:0;width:1200px;height:88px;background:var(--white);display:flex;align-items:center;justify-content:center;font-size:13px;font-weight:600;color:var(--navy);letter-spacing:.5px}
</style>
</head>
<body>

<header class="hero">
  <div class="hero-photo photo" role="img" aria-label="Bright clinic scene with a smiling woman receiving an IV drip"></div>
  <div class="topbar">
    <span class="phone">
      <svg width="12" height="12" viewBox="0 0 24 24"><path fill="#1f2a7a" d="M6.6 10.8a15 15 0 0 0 6.6 6.6l2.2-2.2a1 1 0 0 1 1-.25 11.4 11.4 0 0 0 3.6.57 1 1 0 0 1 1 1V20a1 1 0 0 1-1 1A17 17 0 0 1 3 4a1 1 0 0 1 1-1h3.5a1 1 0 0 1 1 1c0 1.25.2 2.45.57 3.57a1 1 0 0 1-.25 1z"/></svg>
      +61 100 200 300
    </span>
    <span>ENG ▾</span>
  </div>
  <div class="logo"><span class="mark"></span>VELMO</div>
  <nav class="nav">
    <span>Home</span><span>Services</span><span>Treatment</span><span>Locations</span><span>FAQs</span><span>About Us</span>
  </nav>
  <a class="btn book-now" href="#">Book Now</a>
  <h1>Path to Wellness and Rejuvenation</h1>
  <p class="lead">We believe in the power of personalized care and the healing benefits of IV therapy.</p>
  <a class="btn cta" href="#">Book Your Session Today</a>
</header>

<section class="services">
  <div class="service"><div class="photo" role="img" aria-label="Man relaxing during hydration therapy" style="background:linear-gradient(160deg,#8a7a68,#4f4a45)"></div><span>Hydration Therapy</span></div>
  <div class="service active"><div class="photo" role="img" aria-label="Nurse preparing a vitamin infusion" style="background:linear-gradient(160deg,#6a98a8,#2f5a6e)"></div><span>Vitamin Infusions</span></div>
  <div class="service"><div class="photo" role="img" aria-label="Woman with glowing skin after a beauty boost" style="background:linear-gradient(160deg,#d9c0ac,#9c7d68)"></div><span>Beauty Boosts</span></div>
  <div class="service"><div class="photo" role="img" aria-label="Clinician adjusting an IV line for energy therapy" style="background:linear-gradient(160deg,#b9c3cf,#6a7585)"></div><span>Energy &amp; Vitality</span></div>
</section>

<section class="intro">
  <h2>At Velmo Hydration, we believe in the power of personalized care and the healing benefits of IV therapy. Our clinic offers a wide range of cutting-edge IV nutritional treatments designed to boost your vitality, promote recovery, and support overall well-being.</h2>
  <p>Whether you're looking to recharge after an intense workout, recover from a long night, or simply maintain your health, our expert team offers a variety of vitamin-infused IV drips to meet your unique needs. From hydration therapy to immune support, detoxification, and energy boosts, we've got you covered.</p>
  <div class="actions"><a class="btn outline" href="#">View Our Full Menu</a><a class="btn" href="#">Book Your Session</a></div>
</section>

<section class="why">
  <h2 class="section-title">Why Choose Velmo Hydration?</h2>

  <article class="feature f1">
    <div class="photo" role="img" aria-label="Runner silhouetted against a sunset beach" style="background:linear-gradient(180deg,#f2b45a 0%,#e07a2c 55%,#6b3a1e 100%)"></div>
    <div class="copy">
      <h3>Targeted<br>Wellness</h3>
      <p>Our clinic offers a range of IV treatments that provide essential vitamins, minerals, and hydration directly to your bloodstream, allowing for maximum absorption and faster results. Whether you're looking for a detox, immune boost, or energy recharge, we have a solution tailored just for you.</p>
      <a class="btn" href="#">Book an Appointment</a>
    </div>
  </article>

  <article class="feature f2 reverse">
    <div class="photo" role="img" aria-label="Sliced oranges beside an IV drip bag" style="background:linear-gradient(160deg,#eef1f4 0%,#f7c06a 60%,#e8892c 100%)"></div>
    <div class="copy">
      <h3>Customized<br>Treatments</h3>
      <p>Each person is unique, which is why our expert team creates customized IV therapy plans that suit your individual needs. From boosting hydration to replenishing vital nutrients, we ensure that your body gets exactly what it needs to thrive.</p>
      <a class="btn" href="#">Book an Appointment</a>
    </div>
  </article>

  <article class="feature f3">
    <div class="photo" role="img" aria-label="Calm treatment room with patients resting in recliners" style="background:linear-gradient(160deg,#e8edf3,#aebdcc)"></div>
    <div class="copy">
      <h3>Comfortable,<br>Relaxing Environment</h3>
      <p>Your health and comfort are our top priorities. Enjoy our calming, spa-like environment while you receive your treatment. With a dedicated team of licensed professionals, you can rest assured that you're in safe hands.</p>
      <a class="btn" href="#">Book an Appointment</a>
    </div>
  </article>

  <article class="feature f4 reverse">
    <div class="photo" role="img" aria-label="Team of medical professionals in scrubs" style="background:linear-gradient(160deg,#e4e8ee,#4f8f8c 70%,#2f5c5a)"></div>
    <div class="copy">
      <h3>Professional<br>Expertise</h3>
      <p>Our team is made up of certified medical professionals with years of experience. We ensure that your health and safety are our top priorities every step of the way.</p>
      <a class="btn" href="#">Book an Appointment</a>
    </div>
  </article>

  <article class="feature f5">
    <div class="photo" role="img" aria-label="Close-up of an IV drip chamber in blue light" style="background:linear-gradient(160deg,#1d5c8f,#58b3d6 55%,#12324f)"></div>
    <div class="copy">
      <h3>State-of-the-Art<br>Equipment</h3>
      <p>We use the latest technology and high-quality products to ensure the safest and most effective treatments for you. From sterile equipment to premium-grade nutrients, we don't cut corners on your health.</p>
      <a class="btn" href="#">Book an Appointment</a>
    </div>
  </article>
</section>

<section class="reviews">
  <h2 class="section-title">What Our Clients Are Saying</h2>
  <div class="review-row">
    <blockquote class="review">
      <h4>"A Game-Changer for My Recovery!"</h4>
      <p>"I've always struggled with staying hydrated after tough workouts, but after trying Velmo Hydration's IV therapy, I feel like a new person! The team is so knowledgeable and the process was quick and painless. I'll definitely be coming back regularly to boost my recovery."</p>
      <div class="author"><div class="avatar" role="img" aria-label="Client portrait"></div><div><b>Sarah L.</b><i>Fitness Enthusiast</i></div></div>
    </blockquote>
    <blockquote class="review">
      <h4>"Incredible Experience, Highly Recommend!"</h4>
      <p>"I came in for an immune boost before a big trip, and I couldn't be happier with the results. Not only did I feel revitalized, but the staff made me feel incredibly comfortable and well taken care of. I arrived feeling sluggish and left feeling like I could conquer anything!"</p>
      <div class="author"><div class="avatar" role="img" aria-label="Client portrait"></div><div><b>James R.</b><i>Frequent Traveler</i></div></div>
    </blockquote>
  </div>
  <div class="dots"><span></span><span class="on"></span><span class="on"></span><span></span></div>
</section>

<footer class="footer">
  <div class="logo"><span class="mark"></span>VELMO</div>
  <div class="fcol links">
    <h5>Quick Links</h5>
    <ul><li>Home</li><li>FAQs</li><li>Services</li><li>About Us</li><li>Treatment</li><li>Contact Us</li><li>Locations</li><li>Book Now</li></ul>
  </div>
  <div class="fcol reach">
    <h5>Reach Us</h5>
    Country —<br>100 Sample Street, Office 1<br>Sample, SA 10000<br>hello@velmo.example<br>+61 100 200 300
  </div>
  <div class="fcol social">
    <h5>Social Media</h5>
    <div class="socials"><span></span><span></span><span></span><span></span></div>
  </div>
</footer>
<div class="copyright">VELMO HYDRATION © 2025. ALL RIGHTS RESERVED</div>

</body>
</html>
```